updated documents

Hi i have included a new picture for the about us section, i have also included the updated word document, all changes have been highlighted.

Thanks,

Leon

```html
<!DOCTYPE html>
<html lang="en">
<head>
<meta charset="utf-8">
<title>Services Spread</title>
<link rel="stylesheet" href="https://fonts.googleapis.com/css2?family=Crimson+Text:wght@400;600&display=swap">
<style>
  :root {
    --green: #b2d235;
    --grey: #6d6e70;
    --ink: #4a4a4a;
    --body: #545454;
    --paper: #ffffff;
    --backdrop: #2a2a2a;
    --photo-blue: #c9d4dc;
    --photo-wood: #cdb49a;
  }
  html, body {
    margin: 0;
    width: 1200px;
    height: 960px;
    overflow: hidden;
    background: var(--backdrop);
  }
  .spread {
    position: absolute;
    left: 0;
    top: 56px;
    width: 1277px;
    height: 903px;
    background: var(--paper);
    transform: scale(0.9397);
    transform-origin: 0 0;
    font-family: "Crimson Text", Georgia, serif;
    color: var(--body);
  }
  .spread-art { position: absolute; inset: 0; }
  .service { position: absolute; }
  .service-marker {
    position: absolute;
    width: 34px;
    height: 34px;
    border-radius: 50%;
    background: var(--green);
  }
  .service-title {
    position: absolute;
    margin: 0;
    font-weight: 600;
    font-size: 19.5px;
    line-height: 26px;
    color: var(--ink);
    letter-spacing: 0.2px;
    white-space: nowrap;
  }
  .service-text {
    position: absolute;
    margin: 0;
    font-size: 16px;
    line-height: 23px;
    letter-spacing: 0.1px;
  }
</style>
</head>
<body>
<div class="spread">
  <svg class="spread-art" width="1277" height="903" viewBox="0 0 1277 903">
    <defs>
      <linearGradient id="plumbing-tone" x1="0" y1="0" x2="1" y2="1">
        <stop offset="0" stop-color="#e6ecef"/>
        <stop offset="1" stop-color="var(--photo-blue)"/>
      </linearGradient>
      <linearGradient id="carpentry-tone" x1="0" y1="0" x2="1" y2="1">
        <stop offset="0" stop-color="#e9e3d9"/>
        <stop offset="1" stop-color="var(--photo-wood)"/>
      </linearGradient>
    </defs>
    <path fill="var(--green)" fill-rule="evenodd" d="M0 18 L166 178 L0 343 Z M0 118 L65 180 L0 243 Z"/>
    <polygon fill="var(--grey)" points="25,0 935,0 502,473"/>
    <polygon fill="var(--paper)" points="173,0 803,0 502,323"/>
    <polygon fill="url(#plumbing-tone)" points="189,0 788,0 502,311" role="img" aria-label="Photo of a plumber in blue overalls fixing pipes under a basin"/>
    <polygon fill="var(--green)" points="0,903 148,746 247,746 103,903"/>
    <path fill="var(--grey)" fill-rule="evenodd" d="M133 903 L300 726 L483 903 Z M250 903 L300 850 L355 903 Z"/>
    <polygon fill="var(--grey)" points="638,903 805,726 915,726 750,903"/>
    <polygon fill="var(--green)" points="775,903 1153,501 1277,622 1277,903"/>
    <polygon fill="var(--paper)" points="903,903 1157,623 1277,738 1277,903"/>
    <polygon fill="url(#carpentry-tone)" points="918,903 1157,640 1277,755 1277,903" role="img" aria-label="Photo of a carpenter cutting timber with a circular saw"/>
  </svg>

  <section class="service">
    <span class="service-marker" style="left:29px;top:342px"></span>
    <h2 class="service-title" style="left:80px;top:333px">RUBBISH REMOVAL<br>/RECYCLING</h2>
    <p class="service-text" style="left:29px;top:397px;width:368px">If you are looking to make some changes to your office either big or small our team can assist with Workstation reconfiguration, internal demolition, Partition/wall installations and even complete office relocations.</p>
  </section>

  <section class="service">
    <span class="service-marker" style="left:27px;top:569px"></span>
    <h2 class="service-title" style="left:73px;top:573px">PLUMBING</h2>
    <p class="service-text" style="left:29px;top:613px;width:562px">Our Plumbing team are experienced and available 24/7 for all your plumbing requirements. Our plumbing services include, water boiler/chiller unit installs and repairs, blocked drains and toilets, roof work and gas fitting.</p>
  </section>

  <section class="service">
    <span class="service-marker" style="left:928px;top:93px"></span>
    <h2 class="service-title" style="left:982px;top:97px">GROUNDS KEEPING</h2>
    <p class="service-text" style="left:920px;top:142px;width:312px">Let us help with your grounds keeping, our services include, lawn mowing and garden care, carpark sweeping, tree pruning, line marking, gutter cleaning, landscaping, bird and pest management, fencing installs and repairs.</p>
  </section>

  <section class="service">
    <span class="service-marker" style="left:720px;top:325px"></span>
    <h2 class="service-title" style="left:768px;top:329px">CARPENTRY</h2>
    <p class="service-text" style="left:714px;top:371px;width:518px">Keystone Property Services have a dedicated carpentry team that can assist with all your requirements including Partitioning, cupboard installations and all repairs and modifications.</p>
  </section>

  <section class="service">
    <span class="service-marker" style="left:684px;top:525px"></span>
    <h2 class="service-title" style="left:748px;top:529px">FLOOR /CEILING</h2>
    <p class="service-text" style="left:661px;top:568px;width:358px">We can provide floor and ceiling repairs to all types of systems including, suspended ceiling systems and raised floors, ceiling/floor tile replacement, carpet and vinyl replacements and repairs, ceiling access hatches and air vent installs.</p>
  </section>
</div>
</body>
</html>
```